Need a web design for my company which has an existing logo already

Hello,
I am looking for a web designer for my sports and well-being company. I've got a logo already which should be used for the creation. I will need the entire design idea for my word press website (5 -10 pages) .
Please see the attached logo.
My company is a yoga, dance and retreat business, but not only for women. So it shouldn't be girly. I am looking for a neutral design.
I am looking forward to read your proposals. Please show me some samples of similar jobs you have done in the past.
best regards,
Tansy

```html
<!DOCTYPE html>
<html lang="en">
<head>
<meta charset="utf-8">
<title>Stillpoint Studio</title>
<link href="https://fonts.googleapis.com/css2?family=Libre+Baskerville:wght@400;700&family=Roboto:ital,wght@0,400;0,500;0,700;1,400&display=swap" rel="stylesheet">
<style>
:root{
  --sage:#98a48b;
  --sage-dark:#8a9780;
  --sand:#d3cdc8;
  --nav:#d7d2ce;
  --ink:#1f1f1f;
  --muted:#8d8d8d;
  --white:#ffffff;
  --footer:#2e2e2e;
  --contact:#a6ae9b;
}
*{box-sizing:border-box;margin:0;padding:0}
html,body{width:1200px;height:4474px;overflow:hidden}
body{position:relative;font-family:"Roboto",Arial,sans-serif;color:var(--ink);background:var(--white)}
.abs{position:absolute}
.serif{font-family:"Libre Baskerville",Georgia,serif}
.btn{position:absolute;background:var(--sage);color:#fff;font:700 13px "Roboto",Arial,sans-serif;letter-spacing:.5px;text-transform:uppercase;display:flex;align-items:center;justify-content:center;gap:9px;border-radius:2px}
.btn .dot{width:12px;height:12px;border-radius:50%;background:#fff;position:relative}
.btn .dot::after{content:"";position:absolute;left:4px;top:3px;border-left:5px solid var(--sage);border-top:3px solid transparent;border-bottom:3px solid transparent}

/* nav */
.nav{left:0;top:0;width:1200px;height:68px;background:var(--nav);z-index:3}
.brand{left:110px;top:14px;font:400 30px "Libre Baskerville",Georgia,serif;color:#fff;letter-spacing:1px}
.menu{left:298px;top:26px;display:flex;gap:29px;font:500 13px "Roboto",Arial,sans-serif;color:#fff;text-transform:uppercase;letter-spacing:.4px}
.register{left:981px;top:13px;width:108px;height:42px;font-size:13px}

/* hero */
.hero{left:0;top:0;width:1200px;height:625px;background:linear-gradient(180deg,#8fa2a6 0%,#c9cfcb 30%,#a8b99a 55%,#6f8a4c 75%,#5b5a52 100%)}
.hero h1{left:111px;top:238px;font:700 53px "Libre Baskerville",Georgia,serif;color:#fff;letter-spacing:1px}
.hero p{left:112px;top:318px;width:620px;font-size:15px;line-height:28px;color:#fff}
.hero .btn{left:113px;top:394px;width:157px;height:50px}
.arrow{width:44px;height:44px;border-radius:50%;background:#fff;display:flex;align-items:center;justify-content:center}
.arrow.ghost{background:#fff;border:1px solid #e3e3e3;width:42px;height:42px}

/* feature grid */
.tile-img{position:absolute}
.panel{position:absolute;padding:60px 50px 0 50px;color:#fff}
.panel .kicker{font:500 17px "Roboto",Arial,sans-serif;letter-spacing:.5px;text-transform:uppercase}
.panel h3{font:700 20px/30px "Libre Baskerville",Georgia,serif;text-transform:uppercase;margin-top:12px}
.panel p{font-size:13px;line-height:27.5px;margin-top:14px}

/* corporate */
.corp-img{left:0;top:1621px;width:1200px;height:472px;background:linear-gradient(90deg,#7f8590 0%,#a9adb3 35%,#cfd0d2 55%,#f4f4f4 72%,#ffffff 100%)}
.corp h2{left:599px;top:1690px;font:700 33px/40px "Libre Baskerville",Georgia,serif;text-transform:uppercase}
.corp p{left:599px;top:1789px;width:490px;font-size:13.5px;line-height:30px;color:var(--muted)}
.corp .btn{left:598px;top:1967px;width:156px;height:50px}

.section-title{position:absolute;width:1200px;left:0;text-align:center;font:700 33px "Libre Baskerville",Georgia,serif;text-transform:uppercase}

/* video */
.video{left:257px;top:2263px;width:686px;height:386px;background:linear-gradient(180deg,#dfe0e2 0%,#c6c4c3 55%,#8a6a4d 80%,#6f5238 100%)}
.play{left:567px;top:2424px;width:64px;height:64px;border-radius:50%;background:rgba(255,255,255,.55);display:flex;align-items:center;justify-content:center}
.divider{left:0;top:2741px;width:1200px;height:1px;background:#ececec}

/* testimonials */
.card{position:absolute;top:2897px;width:316px;height:212px;background:#fff;border-radius:14px;box-shadow:0 2px 8px rgba(0,0,0,.12);padding:22px 30px 0 30px}
.card.active{background:var(--sage);color:#fff}
.quote{font:700 40px/36px "Libre Baskerville",Georgia,serif;color:#b1b8a8;height:30px}
.card.active .quote{color:#dfe3da}
.card p{font:italic 13.5px/26px "Roboto",Arial,sans-serif;color:#6f6f6f;margin-top:8px}
.card.active p{color:#fff}
.person{display:flex;align-items:center;gap:18px;margin-top:10px}
.avatar{width:46px;height:46px;border-radius:50%;background:linear-gradient(135deg,#5c4a3f,#c4977a)}
.card.active .avatar{background:linear-gradient(135deg,#e6a246,#f2d6a7)}
.person .name{font:500 13.5px "Roboto",Arial,sans-serif;color:#9aa38f;text-transform:uppercase}
.card.active .person .name{color:#fff}
.person .role{font-size:13.5px;color:#6f6f6f}
.card.active .person .role{color:#fff}

/* featured */
.featured{left:0;top:3226px;width:1200px;height:323px;background:linear-gradient(180deg,#d4d0cc,#c8c3bd 60%,#bdb7b0)}
.badge{position:absolute;top:3370px;width:188px;height:108px;background:#fff;display:flex;align-items:center;justify-content:center}
.badge span{display:block;width:70px;height:50px;border-radius:6px;background:#d9d9d9}

/* contact */
.contact{left:0;top:3549px;width:1200px;height:676px;background:linear-gradient(180deg,#a7b09c,#a3ab97 70%,#9ea48f)}
.field{position:absolute;background:#fff;border-radius:2px;font-size:13.5px;color:#6f6f6f;padding:15px 20px}
.outline-btn{left:526px;top:3955px;width:146px;height:47px;border:2px solid #fff;color:#fff;font:500 13px "Roboto",Arial,sans-serif;text-transform:uppercase;display:flex;align-items:center;justify-content:center;gap:9px;border-radius:2px}
.outline-btn .dot{width:12px;height:12px;border-radius:50%;background:#fff}
.info{position:absolute;top:4077px;display:flex;align-items:center;gap:24px;color:#fff;font-size:14px;line-height:22px}
.info .ic{width:66px;height:66px;border-radius:50%;background:#fff;display:flex;align-items:center;justify-content:center}

/* footer */
.footer{left:0;top:4225px;width:1200px;height:249px;background:var(--footer)}
.footer .logo{left:0;width:1200px;top:4268px;text-align:center;font:400 30px "Libre Baskerville",Georgia,serif;color:#fff}
.footer .links{left:0;width:1200px;top:4345px;display:flex;justify-content:center;gap:29px;color:#fff;font:700 13.5px "Roboto",Arial,sans-serif;text-transform:uppercase}
.footer .copy{left:0;width:1200px;top:4401px;text-align:center;color:#fff;font-size:13.5px}
.footer .code{left:1138px;top:4401px;color:#fff;font-size:13px}
</style>
</head>
<body>

<!-- hero -->
<div class="abs hero" role="img" aria-label="Photo of a woman meditating on a deck overlooking misty green mountains"></div>
<h1 class="abs" style="left:111px;top:238px;font:700 53px 'Libre Baskerville',Georgia,serif;color:#fff;letter-spacing:1px">LIVE YOUR BEST LIFE</h1>
<p class="abs" style="left:112px;top:318px;width:620px;font-size:15px;line-height:28px;color:#fff">Lorem ipsum dolor sit amet, consectetur adipiscing elit, sed do eiusmod tempor incididunt ut labore et dolore magna aliqua. Ut enim ad minim veniam</p>
<div class="btn" style="left:113px;top:394px;width:157px;height:50px">Get Started <span class="dot"></span></div>
<div class="abs arrow" style="left:34px;top:324px"><svg width="16" height="16" viewBox="0 0 16 16"><path d="M10 2 4 8l6 6" fill="none" stroke="#111" stroke-width="2.4"/></svg></div>
<div class="abs arrow" style="left:1122px;top:324px"><svg width="16" height="16" viewBox="0 0 16 16"><path d="M6 2l6 6-6 6" fill="none" stroke="#111" stroke-width="2.4"/></svg></div>

<!-- nav -->
<header class="abs nav">
  <div class="abs brand">stillpoint</div>
  <nav class="abs menu"><span>Home</span><span>About Us</span><span>Studio</span><span>Wellness</span><span>Sports</span><span>Contact Us</span>
    <span style="display:flex;gap:8px;align-items:center"><svg width="11" height="12" viewBox="0 0 11 12"><circle cx="5.5" cy="3.2" r="3" fill="#fff"/><path d="M0 12c0-4 2.5-5.5 5.5-5.5S11 8 11 12z" fill="#fff"/></svg>Login</span></nav>
  <div class="btn register">Register</div>
</header>

<!-- wellness / sports grid -->
<div class="tile-img" style="left:101px;top:728px;width:576px;height:396px;background:linear-gradient(135deg,#5e4a3a 0%,#a78669 40%,#e9dfd6 75%,#f3eee9 100%)" role="img" aria-label="Photo of a woman relaxing at a spa with candles and orchids"></div>
<div class="panel" style="left:677px;top:728px;width:423px;height:396px;background:var(--sand)">
  <div class="kicker">Wellness</div>
  <h3>Cutting-edge solutions support physical &amp; mental well-being</h3>
  <p>Lorem ipsum dolor sit amet, consectetur adipiscing elit, sed do eiusmod tempor incididunt ut labore et dolore magna aliqua. Ut enim ad minim veniam, quis nostrud exercitation ullamco laboris nisi ut aliquip ex ea commodo consequat.</p>
</div>
<div class="panel" style="left:101px;top:1124px;width:420px;height:396px;background:var(--sage)">
  <div class="kicker">Professional Sports</div>
  <h3>Physiological insights give you a competitive advantage</h3>
  <p>Lorem ipsum dolor sit amet, consectetur adipiscing elit, sed do eiusmod tempor incididunt ut labore et dolore magna aliqua. Ut enim ad minim veniam, quis nostrud exercitation ullamco laboris nisi ut aliquip ex ea commodo consequat.</p>
</div>
<div class="tile-img" style="left:521px;top:1124px;width:579px;height:396px;background:linear-gradient(160deg,#e8c7a0 0%,#b97a55 35%,#8c4a35 65%,#6d3526 100%)" role="img" aria-label="Photo of an athlete tying a running shoe at sunset"></div>

<!-- corporate -->
<div class="abs corp-img" role="img" aria-label="Photo of a group meditating in a corporate wellness class"></div>
<div class="corp">
  <h2 class="abs" style="left:599px;top:1690px;font:700 33px/40px 'Libre Baskerville',Georgia,serif">CORPORATE WELLNESS<br>COMES TO YOU</h2>
  <p class="abs" style="left:599px;top:1789px;width:490px;font-size:13.5px;line-height:30px;color:var(--muted)">Sed ut perspiciatis unde omnis iste natus error sit voluptatem accusantium doloremque laudantium, totam rem aperiam, eaque ipsa quae ab illo inventore veritatis et quasi architecto beatae vitae dicta sunt explicabo. Nemo enim ipsam voluptatem quia voluptas sit aspernatur aut odit aut fugit, sed quia consequuntur magni dolore</p>
  <div class="btn" style="left:598px;top:1967px;width:156px;height:50px">Learn More <span class="dot"></span></div>
</div>

<!-- why choose us -->
<h2 class="section-title" style="top:2174px">Why Choose Us</h2>
<div class="abs video" role="img" aria-label="Video still of four dancers rehearsing in a bright studio"></div>
<div class="abs play"><svg width="22" height="24" viewBox="0 0 22 24"><circle cx="11" cy="12" r="0" fill="none"/><path d="M5 3l15 9-15 9z" fill="#fff"/></svg></div>
<div class="abs arrow ghost" style="left:158px;top:2433px"><svg width="14" height="14" viewBox="0 0 16 16"><path d="M10 2 4 8l6 6" fill="none" stroke="#111" stroke-width="2"/></svg></div>
<div class="abs arrow ghost" style="left:999px;top:2433px"><svg width="14" height="14" viewBox="0 0 16 16"><path d="M6 2l6 6-6 6" fill="none" stroke="#111" stroke-width="2"/></svg></div>
<div class="abs divider"></div>

<!-- testimonials -->
<h2 class="section-title" style="top:2806px">What Our Users Say</h2>
<div class="card" style="left:111px"><div class="quote">“</div><p>Lorem ipsum dolor sit amet, consectetur adipiscing elit, sed do eiusmod tempor incididunt ut labore et dolor</p><div class="person"><div class="avatar" role="img" aria-label="Portrait photo of the reviewer"></div><div><div class="name">Marcus Hale</div><div class="role">Businessman</div></div></div></div>
<div class="card active" style="left:441px"><div class="quote">“</div><p>Lorem ipsum dolor sit amet, consectetur adipiscing elit, sed do eiusmod tempor incididunt ut labore et dolor</p><div class="person"><div class="avatar" role="img" aria-label="Portrait photo of the reviewer"></div><div><div class="name">Marcus Hale</div><div class="role">Businessman</div></div></div></div>
<div class="card" style="left:771px"><div class="quote">“</div><p>Lorem ipsum dolor sit amet, consectetur adipiscing elit, sed do eiusmod tempor incididunt ut labore et dolor</p><div class="person"><div class="avatar" role="img" aria-label="Portrait photo of the reviewer"></div><div><div class="name">Marcus Hale</div><div class="role">Businessman</div></div></div></div>

<!-- featured -->
<div class="abs featured" role="img" aria-label="Faded photo of a yoga class in the background"></div>
<h2 class="section-title" style="top:3290px">As Featured In</h2>
<div class="badge" style="left:111px"><span></span></div>
<div class="badge" style="left:309px"><span></span></div>
<div class="badge" style="left:507px"><span></span></div>
<div class="badge" style="left:705px"><span></span></div>
<div class="badge" style="left:901px"><span></span></div>

<!-- contact -->
<div class="abs contact" role="img" aria-label="Sage-tinted photo of an athlete's shoes in the background"></div>
<h2 class="section-title" style="top:3626px;color:#fff">Contact Us</h2>
<div class="field" style="left:228px;top:3721px;width:368px;height:49px">Name</div>
<div class="field" style="left:605px;top:3721px;width:368px;height:49px">Company</div>
<div class="field" style="left:228px;top:3780px;width:368px;height:48px">Email</div>
<div class="field" style="left:605px;top:3780px;width:368px;height:48px">Telephone</div>
<div class="field" style="left:228px;top:3839px;width:745px;height:95px">Message</div>
<div class="abs outline-btn">View More <span class="dot"></span></div>

<div class="info" style="left:98px"><div class="ic"><svg width="30" height="30" viewBox="0 0 30 30"><path d="M15 3a8 8 0 0 0-8 8c0 6 8 16 8 16s8-10 8-16a8 8 0 0 0-8-8z" fill="none" stroke="#b7b7b7" stroke-width="2"/><circle cx="15" cy="11" r="3" fill="none" stroke="#b7b7b7" stroke-width="2"/></svg></div><div>Lorem Ipsum Dolor<br>United States</div></div>
<div class="info" style="left:372px"><div class="ic"><svg width="30" height="30" viewBox="0 0 30 30"><rect x="4" y="8" width="22" height="15" fill="none" stroke="#b7b7b7" stroke-width="2"/><path d="M4 8l11 9 11-9" fill="none" stroke="#b7b7b7" stroke-width="2"/></svg></div><div>www.stillpointstudio.example</div></div>
<div class="info" style="left:667px"><div class="ic"><svg width="30" height="30" viewBox="0 0 30 30"><path d="M8 4l5 5-3 3c1 3 4 6 7 7l3-3 5 5-3 4C13 25 5 17 4 7z" fill="none" stroke="#b7b7b7" stroke-width="2"/></svg></div><div>1 555 010 200</div></div>
<div class="info" style="left:915px"><div class="ic"><svg width="30" height="30" viewBox="0 0 30 30"><path d="M8 4l5 5-3 3c1 3 4 6 7 7l3-3 5 5-3 4C13 25 5 17 4 7z" fill="none" stroke="#b7b7b7" stroke-width="2"/></svg></div><div>1 555 010 300</div></div>

<!-- footer -->
<footer class="abs footer"></footer>
<div class="abs" style="left:0;width:1200px;top:4268px;text-align:center;font:400 30px 'Libre Baskerville',Georgia,serif;color:#fff">stillpoint</div>
<div class="abs" style="left:0;width:1200px;top:4345px;display:flex;justify-content:center;gap:29px;color:#fff;font:700 13.5px 'Roboto',Arial,sans-serif"><span>HOME</span><span>ABOUT US</span><span>STUDIO</span><span>WELLNESS</span><span>SPORTS</span><span>CONTACT US</span></div>
<div class="abs" style="left:0;width:1200px;top:4401px;text-align:center;color:#fff;font-size:13.5px">© 2021 Stillpoint Studio. All Rights Reserved</div>
<div class="abs" style="left:1138px;top:4401px;color:#fff;font-size:13px">C42</div>

</body>
</html>
```